Upscale, Elegant Healthy Turmeric Honey Packaging Project for a Startup

We are a startup company based in North Carolina, US. We focus on benefits of Turmeric. We are looking for a packaging design that is elegant, clean looking mostly on white background which would standout on shelf as well as speak to quality of the ingredients and product.Few important points about our product1) All our ingredients are 100% USDA Organic2) Two Types of Honey - 100% Raw Unfiltered Wildflower Honey (Local). It needs to say Made by North Carolina Bees" to stand out as local honey - 100% Organic Raw Honey (non-localized)3) Our honey includes actual raw turmeric roots so this is important to communicate which is the key factor of our product4) We use Hex bottle of 12 Oz and 16 oz classic jar bottleFinal design should be clean, healthy and upscale - should be flexible to accommodate types of honey. 5 ) Back label image is attached. Our organic honey is from Brazil so Product of Brazil or Product of the USA is added to each of the back label.6) Website name needs to be in front of the label and our new website soon to be launch will be www.CrestaleMarket.com 7) We have tag line "Brovique! Bring it to your day!" which is our registered trademark needs to be included in back or front label (help us choose)We have attached some of the current simple example of our labels that we use. Provide design how it would look in the two types of bottles.

Please try to show on a bottle image of bottle (illustration) we use
https://www.vantorelsupply.com/glass-containers/cb1c-classic-glass-jar-1lb.asp for 8 oz and 16 oz
and we use
https://www.vantorelsupply.com/glass-containers/hx12c-12oz-hex-jars-w-63mm-cap.asp for 12 oz

Target Market(s)

upscale retailers, consumers, health & wealth

Colors
fcf9ce
fffbf1
fbca95
ffffff
fefdec

Requirements
Must have
• Clean, elegant look, We prefer white or off white background, Must have way to show that our honey includes raw turmeric or somehow to communicate it is turmeric honey.
Should not have
• Absolutely no similar concept of our current labels should be used in new design. Whole idea is that we are open to adopt creative ways to communicate to our customer about our product so take this as challenge.

```html
<!DOCTYPE html>
<html lang="en">
<head>
<meta charset="utf-8">
<title>Honey with Raw Turmeric – Front Label</title>
<link href="https://fonts.googleapis.com/css2?family=Jost:wght@400;500&family=Libre+Bodoni:wght@400;600&display=swap" rel="stylesheet">
<style>
  :root {
    --canvas-bg: #e9e9e9;
    --label-bg: #f3f2f1;
    --ink: #1f1f1f;
    --gold: #c4952b;
    --band: #c39a3a;
    --band-ink: #3a2a0c;
    --rule: #3a3a3a;
    --sketch-light: #eceae6;
    --sketch-mid: #b9b6b0;
  }
  * { box-sizing: border-box; margin: 0; padding: 0; }
  html, body { width: 923px; height: 1200px; overflow: hidden; }
  body {
    background: var(--canvas-bg);
    position: relative;
    font-family: "Jost", sans-serif;
    color: var(--ink);
  }
  .label {
    position: absolute;
    left: 116px; top: 48px;
    width: 690px; height: 1104px;
    background: var(--label-bg);
    border-radius: 14px;
    overflow: hidden;
    box-shadow: 0 2px 10px rgba(0,0,0,0.08);
  }
  .brand {
    position: absolute;
    top: 92px; left: 0; right: 0;
    display: flex; justify-content: center; align-items: center; gap: 12px;
  }
  .brand-dot {
    width: 22px; height: 22px; border-radius: 50%;
    background: var(--ink);
  }
  .brand-name {
    font-family: "Jost", sans-serif;
    font-weight: 500;
    font-size: 24px;
    color: var(--ink);
  }
  .title {
    position: absolute;
    top: 240px; left: 0; right: 0;
    text-align: center;
    font-family: "Jost", sans-serif;
    font-weight: 400;
    font-size: 66px;
    line-height: 70px;
    letter-spacing: 5px;
    color: var(--ink);
  }
  .title .accent { color: var(--gold); font-weight: 500; }
  .rule {
    position: absolute;
    left: 291px; width: 108px; height: 2px;
    background: var(--rule);
  }
  .rule-top { top: 439px; }
  .rule-bottom { top: 619px; }
  .description {
    position: absolute;
    top: 472px; left: 0; right: 0;
    text-align: center;
  }
  .description .line {
    font-family: "Libre Bodoni", serif;
    font-size: 25px;
    letter-spacing: 3px;
    line-height: 42px;
    color: var(--ink);
  }
  .description .line-accent {
    font-family: "Jost", sans-serif;
    font-size: 28px;
    letter-spacing: 1.5px;
    line-height: 42px;
    color: var(--gold);
  }
  .ingredients-art {
    position: absolute;
    top: 640px; left: 0;
    width: 690px; height: 270px;
  }
  .info-band {
    position: absolute;
    top: 914px; left: 0;
    width: 690px; height: 136px;
    background: var(--band);
    display: flex; align-items: center;
  }
  .info-cell {
    height: 100%;
    display: flex; align-items: center; justify-content: center;
    text-align: center;
    color: var(--band-ink);
  }
  .net-weight { width: 280px; font-size: 22px; }
  .origin {
    width: 236px;
    border-left: 2px solid var(--band-ink);
    border-right: 2px solid var(--band-ink);
    height: 104px;
    font-family: "Libre Bodoni", serif;
    font-size: 19px; letter-spacing: 3px; line-height: 30px;
  }
  .origin strong { font-weight: 600; }
  .certification { flex: 1; }
  .cert-badge {
    width: 92px; height: 92px; border-radius: 50%;
    background: #f7f1e2;
    border: 5px solid #1f1f1f;
  }
  .website {
    position: absolute;
    top: 1064px; left: 0; right: 0;
    text-align: center;
    font-size: 15px; letter-spacing: 1.5px;
    color: #444;
  }
</style>
</head>
<body>
  <main class="label">
    <div class="brand">
      <span class="brand-dot"></span>
      <span class="brand-name">Aurelle Honey</span>
    </div>

    <h1 class="title">HONEY WITH<br>RAW <span class="accent">TURMERIC</span></h1>

    <div class="rule rule-top"></div>
    <div class="description">
      <p class="line">100% ORGANIC RAW HONEY</p>
      <p class="line">WITH TURMERIC ROOTS</p>
      <p class="line-accent">WITH CEYLON CINNAMON &amp; CLOVES</p>
    </div>
    <div class="rule rule-bottom"></div>

    <svg class="ingredients-art" viewBox="0 0 690 270" role="img" aria-label="Engraved sketch of turmeric roots, cinnamon sticks, leaves and honey bees">
      <defs>
        <linearGradient id="sketchFade" x1="0" y1="0" x2="0" y2="1">
          <stop offset="0" stop-color="var(--label-bg)"/>
          <stop offset="0.45" stop-color="var(--sketch-light)"/>
          <stop offset="1" stop-color="var(--sketch-mid)"/>
        </linearGradient>
      </defs>
      <rect width="690" height="270" fill="url(#sketchFade)"/>
    </svg>

    <section class="info-band">
      <div class="info-cell net-weight">Net Wt. 16 oz(454g)</div>
      <div class="info-cell origin"><p>MADE BY<br><strong>BRAZILIAN</strong><br><strong>BEES</strong></p></div>
      <div class="info-cell certification"><span class="cert-badge"></span></div>
    </section>

    <p class="website">www.CrestaleMarket.com</p>
  </main>
</body>
</html>
```